An image to show that our fees are offset by our good management

We work in the property sector.
We'd like a slide showing that our fees weigh very little compared with the savings we can generate if we do our job properly as property managers.
To do this, we've come up with a slide with a scale showing our fees on the left (which weigh less or the same) than the items on the right.
On the right you can see:
Savings on building maintenance costs
Savings on running costs
Optimization of vacant periods
Good monitoring of disputes to avoid rental losses
We welcome any other ideas you may have to highlight this concept (even off-balance sheet).

```html
<!DOCTYPE html>
<html lang="en">
<head>
<meta charset="utf-8">
<title>Fees Offset by Our Good Management</title>
<link href="https://fonts.googleapis.com/css2?family=Poppins:wght@400;500;700;800&family=Oswald:wght@600&display=swap" rel="stylesheet">
<style>
  :root {
    --orange: #cf5a1c;
    --band-dark: #3b3b3b;
    --headline-yellow: #f6dc12;
    --ink: #1f1f1f;
    --white: #ffffff;
    --step-yellow: #f1c20a;
    --step-green: #23935a;
    --step-orange: #d9622a;
    --step-blue: #1c1ae6;
    --block-dark: #262626;
    --label-yellow: #f2b200;
    --label-green: #1f8f4e;
    --label-orange: #d9590e;
    --label-blue: #1a16e0;
    --rule: #555555;
  }
  html, body { margin: 0; padding: 0; overflow: hidden; background: var(--white); }
  .slide {
    position: relative;
    width: 1200px;
    height: 1056px;
    overflow: hidden;
    background: var(--white);
    font-family: "Poppins", sans-serif;
    color: var(--ink);
  }
  .desk-backdrop {
    position: absolute;
    left: 679px; top: 49px;
    width: 521px; height: 300px;
    background: radial-gradient(ellipse at 70% 30%, #ece8e2 0%, #f6f4f1 45%, rgba(255,255,255,0) 80%);
  }
  .header-band { position: absolute; left: 0; top: 0; width: 1200px; height: 250px; }
  .header-kicker {
    position: absolute; left: 62px; top: 64px; margin: 0;
    font-weight: 400; font-size: 35px; letter-spacing: 5px; color: var(--white);
    line-height: 1;
  }
  .header-title { position: absolute; left: 58px; top: 118px; }
  .header-title text { font-family: "Oswald", sans-serif; font-weight: 600; fill: var(--headline-yellow); }
  .intro {
    position: absolute; left: 62px; top: 254px; margin: 0;
    font-size: 20.5px; line-height: 29.5px; font-weight: 400; white-space: nowrap;
  }
  .seesaw {
    position: absolute; left: 57px; top: 690px; width: 1082px; height: 320px;
    background: radial-gradient(ellipse at 50% 25%, #b9b9b9 0%, #d4d4d4 35%, #ececec 60%, rgba(255,255,255,0) 80%);
  }
  .fees-label { position: absolute; left: 60px; top: 462px; margin: 0; line-height: 1.08; }
  .fees-label .our { display: block; font-size: 50px; font-weight: 500; color: var(--ink); letter-spacing: -1px; }
  .fees-label .fees { display: block; font-size: 50px; font-weight: 800; color: var(--label-green); letter-spacing: -1px; }
  .money-bag {
    position: absolute; left: 200px; top: 412px; width: 290px; height: 318px;
    border-radius: 40% 40% 30% 30%;
    background: radial-gradient(circle at 62% 55%, #9a9592 0%, #b4aea9 45%, #f2c94c 78%, rgba(255,255,255,0) 92%);
  }
  .steps { position: absolute; left: 0; top: 0; }
  .step-number { font-family: "Poppins", sans-serif; font-weight: 800; font-size: 50px; fill: var(--white); }
  .benefits { position: absolute; left: 887px; top: 0; width: 270px; margin: 0; padding: 0; list-style: none; }
  .benefit {
    position: absolute; left: 0; width: 270px; white-space: nowrap;
    font-size: 25px; line-height: 29px; font-weight: 400; color: var(--ink);
  }
  .benefit strong { font-weight: 700; }
  .benefit--maintenance { top: 283px; }
  .benefit--maintenance strong { color: var(--label-yellow); }
  .benefit--running { top: 401px; }
  .benefit--running strong { color: var(--label-green); }
  .benefit--vacancy { top: 521px; }
  .benefit--vacancy strong { color: var(--label-orange); }
  .benefit--disputes { top: 643px; }
  .benefit--disputes strong { color: var(--label-blue); }
  .rule { position: absolute; left: 887px; width: 250px; border-top: 1.5px dashed var(--rule); }
  .rule--first { top: 372px; }
  .rule--second { top: 494px; }
  .rule--third { top: 615px; }
  .footer-band { position: absolute; left: 0; bottom: 0; width: 1200px; height: 14px; background: var(--orange); }
</style>
</head>
<body>
<div class="slide">
  <div class="desk-backdrop" role="img" aria-label="Faint photo of a desk with keyboard and glasses"></div>

  <svg class="header-band" width="1200" height="250" viewBox="0 0 1200 250">
    <polygon points="0,36 1200,36 1200,49 700,49 596,245 0,245" fill="var(--band-dark)"/>
    <polygon points="0,0 1200,0 1200,36 686,36 582,233 0,233" fill="var(--orange)"/>
  </svg>
  <p class="header-kicker">FEES OFFSET BY OUR</p>
  <svg class="header-title" width="520" height="82" viewBox="0 0 520 82">
    <text x="0" y="74" font-size="86" textLength="514" lengthAdjust="spacingAndGlyphs">GOOD MANAGEMENT</text>
  </svg>

  <p class="intro">Our fees weigh very little compared with<br>the savings we can generate if we do our job<br>properly as property managers.</p>

  <div class="seesaw" role="img" aria-label="Illustration of a grey seesaw tilted with the fees side raised"></div>

  <p class="fees-label"><span class="our">OUR</span><span class="fees">FEES</span></p>

  <div class="money-bag" role="img" aria-label="Illustration of a money bag with stacks of gold coins"></div>

  <svg class="steps" width="1200" height="1056" viewBox="0 0 1200 1056">
    <rect x="648" y="256" width="218" height="494" rx="16" fill="var(--block-dark)"/>
    <polygon points="692,133 754,235 737,235 737,380 648,380 648,235 633,235" fill="var(--step-yellow)"/>
    <g fill="none" stroke="var(--ink)" stroke-width="2">
      <circle cx="678" cy="328" r="14"/>
      <circle cx="678" cy="328" r="7"/>
      <rect x="696" y="294" width="20" height="52"/>
      <rect x="710" y="306" width="14" height="40"/>
    </g>
    <text class="step-number" x="808" y="332" text-anchor="middle">01</text>
    <polygon points="754,355 866,355 866,502 745,502 745,372" fill="var(--step-green)"/>
    <g fill="none" stroke="var(--white)" stroke-width="2">
      <polygon points="806,400 836,411 806,422 776,411"/>
      <circle cx="806" cy="437" r="16"/>
      <text x="806" y="444" font-size="20" fill="var(--white)" stroke="none" text-anchor="middle" font-family="Poppins, sans-serif">$</text>
    </g>
    <text class="step-number" x="704" y="446" text-anchor="middle">02</text>
    <polygon points="648,480 728,480 740,500 737,627 648,627" fill="var(--step-orange)"/>
    <g fill="none" stroke="var(--white)" stroke-width="2">
      <path d="M692,532 L714,541 L714,560 Q714,580 692,590 Q670,580 670,560 L670,541 Z"/>
      <circle cx="692" cy="561" r="11"/>
      <path d="M692,555 L692,561 L697,564"/>
    </g>
    <text class="step-number" x="814" y="570" text-anchor="middle">03</text>
    <polygon points="754,602 866,602 866,779 745,779 745,618" fill="var(--step-blue)"/>
    <g fill="none" stroke="var(--white)" stroke-width="2">
      <rect x="776" y="654" width="60" height="36" rx="2"/>
      <path d="M798,690 L795,700 L817,700 L814,690"/>
      <circle cx="806" cy="656" r="13" fill="var(--step-blue)"/>
      <path d="M806,649 L806,656 L812,659"/>
    </g>
    <text class="step-number" x="705" y="700" text-anchor="middle">04</text>
  </svg>

  <ul class="benefits">
    <li class="benefit benefit--maintenance"><strong>SAVINGS</strong> on building<br>maintenance costs</li>
    <li class="benefit benefit--running"><strong>SAVINGS</strong> on<br>running costs</li>
    <li class="benefit benefit--vacancy"><strong>OPTIMIZATION</strong> of<br>vacant periods</li>
    <li class="benefit benefit--disputes"><strong>GOOD MONITORING</strong><br>of disputes to avoid<br>rental losses</li>
  </ul>
  <div class="rule rule--first"></div>
  <div class="rule rule--second"></div>
  <div class="rule rule--third"></div>

  <div class="footer-band"></div>
</div>
</body>
</html>
```